Design logo, business cards and letterhead for my eye surgery (doctor's) practice

I am a young eye surgeon (Ophthalmic Surgeon) and I need business cards and letterhead designed ( I have a business card brief and a stationary brief submitted). A small logo would also be useful, or some shape that is seen on both the cards and the letterhead. I am based in Perth, Western Australia. I do some laser refractive work ie LASIK, but also other aspects of ophthalmology as well. The design should be conservative, professional and classic, but also, (as someone who sees young patients for laser surgery) a little interesting to people who refer to me and to patients who will be given my card. The details on the letterhead should be:
Dr Ned Palliser
MBBS (Hons), MMed, FRANZCO
Ophthalmic Surgeon

27 Waverton Ave, Subiaco
Western Australia 6008
Phone: (08) 9217 4602
Facsimile: (08) 9217 4619
Email: reception@nedpalliser.com.au
Provider No: 618095KW

The information on the cards should be the same, but with out the provider number.
On the back of the card should say-

Next Appointment________
The rooms can be accessed easily via public transport, or please feel free to park behind the premises in the designated parking bays.

Target Market(s)

General practitioners and optometrists who refer to me and patients

Industry/Entity Type

Business

Contact Information for Business Card

See above

Requirements
Nice to have
• I've attached a little photo which I thought may make a cute logo of sorts on the cards and letterhead.

```html
<!DOCTYPE html>
<html lang="en">
<head>
<meta charset="utf-8">
<title>Dr Ned Palliser – Business Card</title>
<link rel="stylesheet" href="https://fonts.googleapis.com/css2?family=Alegreya:wght@400;500&family=Michroma&family=Cabin:wght@400&display=swap">
<style>
  :root {
    --canvas: #ecebe8;
    --card: #0b0b0b;
    --red: #d6262e;
    --grey: #8e8e8e;
    --grey-soft: #7a7a7a;
    --white: #f2f2f2;
    --shadow: rgba(0, 0, 0, 0.28);
  }
  * { box-sizing: border-box; margin: 0; padding: 0; }
  html, body { width: 1200px; height: 900px; overflow: hidden; }
  body {
    background: var(--canvas);
    position: relative;
    font-family: "Alegreya", Georgia, serif;
  }

  .card {
    position: absolute;
    width: 620px;
    height: 354px;
    background: var(--card);
    box-shadow: 0 10px 28px var(--shadow);
    overflow: hidden;
  }
  .card--back  { left: 80px;  top: 80px; }
  .card--front { left: 500px; top: 466px; }

  /* practice mark: name with one plain circle */
  .mark {
    display: flex;
    align-items: center;
    gap: 12px;
    font-family: "Alegreya", Georgia, serif;
    font-weight: 500;
    font-size: 30px;
    color: var(--grey);
    letter-spacing: 0.5px;
  }
  .mark__dot {
    width: 26px;
    height: 26px;
    border-radius: 50%;
    background: var(--red);
    flex: none;
  }

  /* back of card */
  .card--back .mark {
    position: absolute;
    top: 78px;
    left: 0;
    right: 0;
    justify-content: center;
  }
  .appointment {
    position: absolute;
    left: 120px;
    top: 226px;
    color: var(--red);
    font-size: 14px;
    display: flex;
    align-items: flex-end;
  }
  .appointment__line {
    display: inline-block;
    width: 196px;
    border-bottom: 1px solid var(--red);
    margin-left: 4px;
    margin-bottom: 3px;
  }
  .directions {
    position: absolute;
    left: 120px;
    top: 262px;
    width: 470px;
    color: var(--red);
    font-size: 14px;
    line-height: 1.3;
  }

  /* front of card */
  .card--front .mark {
    position: absolute;
    left: 92px;
    top: 70px;
  }
  .identity {
    position: absolute;
    left: 92px;
    top: 140px;
  }
  .identity__name {
    font-family: "Michroma", "Arial", sans-serif;
    color: var(--red);
    font-size: 17px;
    text-transform: uppercase;
    letter-spacing: 1px;
    line-height: 1.2;
  }
  .identity__credentials {
    font-family: "Cabin", "Helvetica", sans-serif;
    color: var(--grey);
    font-size: 15px;
    line-height: 1.3;
  }
  .identity__role {
    font-family: "Cabin", "Helvetica", sans-serif;
    color: var(--grey-soft);
    font-size: 15px;
    padding-left: 50px;
    line-height: 1.3;
  }
  .contact {
    position: absolute;
    left: 92px;
    top: 240px;
    color: var(--white);
    font-size: 16px;
    line-height: 1.45;
  }
  .contact__label { color: var(--red); }
  .contact__web { color: var(--red); }
</style>
</head>
<body>

  <section class="card card--back" aria-label="Business card, reverse">
    <div class="mark">
      <span class="mark__dot"></span>
      <span class="mark__name">Palliser Eye</span>
    </div>
    <p class="appointment">Next Appointment<span class="appointment__line"></span></p>
    <p class="directions">The rooms can be accessed easily via public transport, or please feel free to park behind the premises in the designated parking bays.</p>
  </section>

  <section class="card card--front" aria-label="Business card, front">
    <div class="mark">
      <span class="mark__dot"></span>
      <span class="mark__name">Palliser Eye</span>
    </div>
    <div class="identity">
      <h1 class="identity__name">Dr Ned Palliser</h1>
      <p class="identity__credentials">MBBS (Hons), MMed, FRANZCO</p>
      <p class="identity__role">Ophthalmic Surgeon</p>
    </div>
    <div class="contact">
      <p>1234, Address GoesHere, Country, 12345</p>
      <p><span class="contact__label">T:</span> (044) 123 456 789 &nbsp;<span class="contact__label">F:</span> (044) 123456789 &nbsp;<span class="contact__label">M:</span> (044)123456789</p>
      <p><span class="contact__label">E:</span> info@youremail.com &nbsp;<span class="contact__web">www.yourweb.com</span></p>
    </div>
  </section>

</body>
</html>
```